Ruvo Decor

There is a sample provided with the arabic text of the business card. please copy paste the same text and the same Logo (The two triangles) Just try to incorproate the Brown background attached (you are free to change the colors) Id like the colors to be mainly shades of black and red.

```html
<!DOCTYPE html>
<html lang="ar">
<head>
<meta charset="utf-8">
<title>Ruvo Decor – Business Card</title>
<link rel="stylesheet" href="https://fonts.googleapis.com/css2?family=Aref+Ruqaa:wght@400;700&family=Roboto:wght@500&family=Tajawal:wght@500;700&display=swap">
<style>
  :root {
    --page: #ece8e4;
    --red: #cc1f45;
    --red-light: #e04a66;
    --red-deep: #a3122f;
    --black: #141214;
    --black-soft: #2a2628;
    --white: #ffffff;
    --shadow: rgba(0, 0, 0, 0.35);
  }
  * { margin: 0; padding: 0; box-sizing: border-box; }
  html, body {
    width: 1125px; height: 1200px; overflow: hidden;
    background: var(--page);
  }
  .canvas { position: relative; width: 1125px; height: 1200px; }

  .card {
    position: absolute; left: 170px; width: 826px; height: 472px;
    overflow: hidden;
    background: linear-gradient(160deg, var(--red) 0%, var(--red-deep) 100%);
    box-shadow: 0 3px 8px var(--shadow);
    color: var(--white);
    font-family: "Tajawal", sans-serif;
  }
  .card--front { top: 106px; }
  .card--back { top: 640px; }

  .card__texture {
    position: absolute; inset: 0;
    background:
      radial-gradient(ellipse 45% 55% at 75% 35%, rgba(240, 110, 130, 0.45), transparent 70%),
      radial-gradient(ellipse 40% 50% at 20% 30%, rgba(240, 110, 130, 0.35), transparent 70%),
      radial-gradient(ellipse 60% 40% at 50% 100%, rgba(90, 0, 20, 0.35), transparent 70%);
  }

  .card__triangle { position: absolute; inset: 0; width: 100%; height: 100%; }

  .holder {
    position: absolute; left: 30px; top: 40px; width: 266px;
    text-align: right; direction: rtl;
  }
  .holder__name {
    font-family: "Aref Ruqaa", serif; font-weight: 700;
    font-size: 25px; line-height: 1.2;
  }
  .holder__role {
    font-family: "Aref Ruqaa", serif; font-size: 17px;
    margin-top: 6px; margin-right: 60px;
  }
  .holder__phone {
    direction: ltr; text-align: left;
    margin-top: 20px; margin-left: 17px;
    font-family: "Roboto", sans-serif; font-weight: 500; font-size: 20px;
    display: flex; align-items: center; gap: 6px;
  }
  .holder__phone svg { width: 18px; height: 18px; fill: var(--white); }

  .credentials {
    position: absolute; right: 36px; top: 44px;
    direction: rtl; text-align: right;
    font-size: 18px; line-height: 27.5px; letter-spacing: 0.3px;
    list-style: none;
  }

  .brand {
    position: absolute; left: 0; width: 832px; top: 385px;
    text-align: center;
    font-family: "Tajawal", sans-serif; font-weight: 700;
    font-size: 42px; letter-spacing: 1px;
    color: var(--white);
  }
  .brand__mark {
    display: block; width: 16px; height: 16px; margin: 0 auto 14px;
    border-radius: 50%; background: var(--white);
  }

  .services {
    position: absolute; left: 60px; top: 98px; width: 330px;
    list-style: none; direction: rtl; text-align: right;
    font-size: 23px; line-height: 32.3px; letter-spacing: 0.3px;
  }
  .services li::after {
    content: ""; display: inline-block;
    width: 7px; height: 7px; border-radius: 50%;
    background: var(--white);
    margin-right: 12px; vertical-align: middle;
  }
</style>
</head>
<body>
<main class="canvas">

  <section class="card card--front" aria-label="Front of business card">
    <div class="card__texture" role="img" aria-label="Soft red glowing grid of small squares and dots"></div>
    <svg class="card__triangle" viewBox="0 0 826 472" aria-hidden="true">
      <defs>
        <linearGradient id="tri-shade" x1="0" y1="0" x2="0" y2="1">
          <stop offset="0" stop-color="#141214"/>
          <stop offset="0.5" stop-color="#2a2628"/>
          <stop offset="1" stop-color="#141214"/>
        </linearGradient>
      </defs>
      <polygon points="416,0 690,472 143,472" fill="url(#tri-shade)"/>
    </svg>

    <div class="holder">
      <p class="holder__name">المهندس / سامر نبيل الراشد</p>
      <p class="holder__role">أستاذ جامعي</p>
      <p class="holder__phone">
        <svg viewBox="0 0 24 24" aria-hidden="true"><path d="M6.6 10.8a15.1 15.1 0 0 0 6.6 6.6l2.2-2.2a1 1 0 0 1 1-.25 11.4 11.4 0 0 0 3.6.57 1 1 0 0 1 1 1V20a1 1 0 0 1-1 1A17 17 0 0 1 3 4a1 1 0 0 1 1-1h3.5a1 1 0 0 1 1 1c0 1.25.2 2.45.57 3.57a1 1 0 0 1-.25 1z"/></svg>
        30245517 / 60318842
      </p>
    </div>

    <ul class="credentials">
      <li>ماجستير هندسة ديكور</li>
      <li>دبلوم عالي فن تشكيلي</li>
      <li>جامعة الفنون العليا (ليون)</li>
      <li>استشارات هندسية - فنية</li>
    </ul>

    <p class="brand"><span class="brand__mark" aria-hidden="true"></span>Ruvo Decor</p>
  </section>

  <section class="card card--back" aria-label="Back of business card">
    <div class="card__texture" role="img" aria-label="Soft red glowing grid of small squares and dots"></div>
    <ul class="services">
      <li>ماجستير هندسة ديكور</li>
      <li>دبلوم عالي فن تشكيلي</li>
      <li>جامعة الفنون العليا (ليون)</li>
      <li>استشارات هندسية - فنية</li>
      <li>ماجستير هندسة ديكور</li>
      <li>دبلوم عالي فن تشكيلي</li>
      <li>جامعة الفنون العليا (ليون)</li>
      <li>استشارات هندسية - فنية</li>
    </ul>
  </section>

</main>
</body>
</html>
```